Home Builder and Trade Supplier needs a Ad/leaflet/mail drop off leaflet design

BrimHaven is a business that builds homes, renovations, property maintenance and anything else construction related to residential homes. See photos I have attached that have a description of the business.

I'm after a double sided flyer for mail box drop offs. The market audience is up market expensive homes and offices. I have attached some examples of what i think would look good - I would like to see an example like or similar to that but by all means the designs you submit don't have to be a copy or similar. If you have something completely different in mind that you think would suit, please submit or even a rough draft if youre not sure I'll like it and you don't want to risk wasting time.

Please include the text and information in your designs that I have included in my examples.

Submissions before the 10 days are welcome and encouraged :)

Any questions, please feel free to ask on here or through email on: tomas.k@mailnest.example

Pamphlet Size: 210 x 142mm (a quarter of an A4)
Double Sided Colour

Property Maintenance

Requirements
Must have
• Contact Us: 0417 582 916
www.brimhavenhomes.example.au
Double sided
Colour
Size: quater of an A4

```html
<!DOCTYPE html>
<html lang="en">
<head>
<meta charset="utf-8">
<title>BrimHaven – Leaflet</title>
<link href="https://fonts.googleapis.com/css2?family=Open+Sans:ital,wght@0,300;0,400;0,600;1,300&family=Kalam:wght@400&family=Bitter:wght@400&display=swap" rel="stylesheet">
<style>
:root{
  --orange:#f15a22;
  --grey:#b9b9b9;
  --ink:#3a3a3a;
  --soft:#6d6d6d;
  --page:#ffffff;
  --backdrop:#e9e6e2;
  --tool:#231f20;
}
*{margin:0;padding:0;box-sizing:border-box}
html,body{width:1200px;height:872px;overflow:hidden;background:var(--backdrop)}
.canvas{position:relative;width:1200px;height:872px;font-family:"Open Sans",sans-serif;color:var(--ink)}
.page{position:absolute;top:61px;width:513px;height:759px;background:var(--page);box-shadow:0 2px 8px rgba(0,0,0,.18);overflow:hidden}
.front{left:60px}
.back{left:632px}

/* front */
.tool-ring{position:absolute;inset:0;background:radial-gradient(ellipse 62% 58% at 50% 50%, #fff 68%, #8a8687 86%, var(--tool) 100%)}
.brand{display:flex;align-items:center;position:absolute;white-space:nowrap}
.brand-mark{background:var(--grey);flex:none}
.brand-name{font-family:"Open Sans",sans-serif;font-weight:300;color:var(--orange);line-height:1}
.front .brand{left:100px;top:336px;gap:12px}
.front .brand-mark{width:66px;height:84px}
.front .brand-name{font-size:54px}

/* back */
.back .brand{left:34px;top:32px;gap:10px}
.back .brand-mark{width:36px;height:48px}
.back .brand-name{font-size:30px}
.contact-title{position:absolute;left:254px;top:26px;font-family:"Kalam",cursive;color:var(--orange);font-size:27px;transform:rotate(-6deg);transform-origin:left bottom;white-space:nowrap}
.contact-phone{position:absolute;left:292px;top:58px;font-weight:300;font-style:italic;color:var(--grey);font-size:27px;letter-spacing:1px;white-space:nowrap}
.intro{position:absolute;left:18px;right:14px;top:104px;font-size:11.8px;line-height:15px;letter-spacing:-.1px;color:var(--ink)}
.intro p+p{margin-top:8px}
.services{position:absolute;left:14px;top:187px;width:485px;display:grid;grid-template-columns:repeat(5,1fr);grid-auto-rows:108px}
.service{display:flex;flex-direction:column;align-items:center;text-align:center;font-size:12px;line-height:13px;white-space:nowrap}
.service-photo{width:72px;height:72px;border-radius:9px;border:1.5px solid #cfcfcf;box-shadow:0 1px 3px rgba(0,0,0,.25);margin-bottom:5px}
.contact-for{position:absolute;left:13px;top:612px;font-size:15px}
.contact-list{position:absolute;left:13px;top:636px;width:490px;display:grid;grid-template-columns:102px 113px 111px 90px 74px;grid-auto-flow:column;grid-template-rows:repeat(4,18.5px);list-style:none;font-size:12px;color:var(--ink);white-space:nowrap}
.contact-list li::before{content:"•";margin-right:5px}
.web-band{position:absolute;left:0;right:0;bottom:0;height:46px;background:var(--orange);color:#fff;font-family:"Bitter",serif;font-size:23px;display:flex;align-items:center;justify-content:center;letter-spacing:.3px}
</style>
</head>
<body>
<div class="canvas">

  <section class="page front">
    <div class="tool-ring" role="img" aria-label="Ring of black hand-tool silhouettes around the page edges: pliers, spanners, saw, hammers, drills, clamps and shears"></div>
    <div class="brand">
      <span class="brand-mark"></span>
      <span class="brand-name">BrimHaven</span>
    </div>
  </section>

  <section class="page back">
    <div class="brand">
      <span class="brand-mark"></span>
      <span class="brand-name">BrimHaven</span>
    </div>
    <div class="contact-title">Contact Us!</div>
    <div class="contact-phone">0417 582 916</div>

    <div class="intro">
      <p>BrimHaven is one of the preferred home builders and residential trade supplier for customers across Sydney. A one stop shop, We can built your entire home or supply you with our trademen.</p>
      <p>No matter how small or large your job is, contact us to find out how we can help you</p>
    </div>

    <div class="services">
      <div class="service"><span class="service-photo" role="img" aria-label="Technical drawing with compass" style="background:linear-gradient(135deg,#e4e4df,#9a9a92)"></span>Engineering</div>
      <div class="service"><span class="service-photo" role="img" aria-label="Yellow hard hat on plans" style="background:linear-gradient(135deg,#f3d46a,#c98a10)"></span>Project<br>Management</div>
      <div class="service"><span class="service-photo" role="img" aria-label="Tool belt with tools" style="background:linear-gradient(135deg,#b08a5a,#4b3a2a)"></span>Property<br>Maintenance</div>
      <div class="service"><span class="service-photo" role="img" aria-label="Blue house model" style="background:linear-gradient(135deg,#f2f6fb,#3b63c4)"></span>New Homes</div>
      <div class="service"><span class="service-photo" role="img" aria-label="Electrical wires and pliers" style="background:linear-gradient(135deg,#eae4e4,#b3474a)"></span>Electrician</div>

      <div class="service"><span class="service-photo" role="img" aria-label="Paint colour swatches and roller" style="background:linear-gradient(135deg,#3a87c9,#e2a23a,#d24a4a)"></span>Painter</div>
      <div class="service"><span class="service-photo" role="img" aria-label="Grey floor tiles" style="background:linear-gradient(135deg,#7a7f85,#3c4046)"></span>Tilling</div>
      <div class="service"><span class="service-photo" role="img" aria-label="Garden tools and hose" style="background:linear-gradient(135deg,#f1f1ec,#3aa24a)"></span>Landscaping</div>
      <div class="service"><span class="service-photo" role="img" aria-label="Brick wall with trowel" style="background:linear-gradient(135deg,#f3f1ee,#b4502f)"></span>Bricklaying</div>
      <div class="service"><span class="service-photo" role="img" aria-label="Concrete driveway" style="background:linear-gradient(135deg,#d8d8d2,#7d8a6a)"></span>Concreting</div>

      <div class="service"><span class="service-photo" role="img" aria-label="Glass office tower" style="background:linear-gradient(135deg,#bcdcf2,#1d5fa3)"></span>Commercial<br>Fitouts</div>
      <div class="service"><span class="service-photo" role="img" aria-label="Colourful shopping bags" style="background:linear-gradient(135deg,#f0c24a,#d6413f,#3c78c8)"></span>Retail Fitouts</div>
      <div class="service"><span class="service-photo" role="img" aria-label="Excavator bucket" style="background:linear-gradient(135deg,#e6e4e0,#5a534c)"></span>Demolition And<br>Exavation</div>
      <div class="service"><span class="service-photo" role="img" aria-label="Roof shingles" style="background:linear-gradient(135deg,#d0d0cc,#6f706e)"></span>Roofing</div>
      <div class="service"><span class="service-photo" role="img" aria-label="Glass building facade" style="background:linear-gradient(135deg,#e3f1ef,#6fa8a4)"></span>Glazing</div>

      <div class="service"><span class="service-photo" role="img" aria-label="Curved modern building" style="background:linear-gradient(135deg,#dfe9f3,#8a98a6)"></span>Architecture</div>
      <div class="service"><span class="service-photo" role="img" aria-label="Timber fence" style="background:linear-gradient(135deg,#9b6a4d,#4b2f22)"></span>Fencing</div>
      <div class="service"><span class="service-photo" role="img" aria-label="Timber boards and level" style="background:linear-gradient(135deg,#f2d39a,#c58a3c)"></span>Carpentry</div>
      <div class="service"><span class="service-photo" role="img" aria-label="Showroom with feature wall" style="background:linear-gradient(135deg,#e8c23a,#2d4f8c)"></span>3D Feature Walls</div>
      <div class="service"><span class="service-photo" role="img" aria-label="Bathroom fittings and pipe wrench" style="background:linear-gradient(135deg,#f4f4f4,#b2444a)"></span>Plumbing</div>
    </div>

    <div class="contact-for">Contact Us for:</div>
    <ul class="contact-list">
      <li>New Homes</li><li>Renovations</li><li>Architecture</li><li>Engineering</li>
      <li>Maintenance</li><li>Strata</li><li>Air Conditioning</li><li>Plumbing</li>
      <li>Painting</li><li>Electrical</li><li>Lown Mowing</li><li>Landscaping</li>
      <li>Tiling</li><li>Glazing</li><li>Bricklaying</li><li>Roofing</li>
      <li>Demolition</li><li>Excavation</li><li>Carpentry</li><li>Cleaning</li>
    </ul>

    <div class="web-band">www.brimhavenhomes.example.au</div>
  </section>

</div>
</body>
</html>
```